Yoga class opening. Little schedule for JUNE JULY and AUGUST

Flyer to promote an opening yoga class. The color of the docx haven't to be respected.

We want something joyfull, professional, clean and serious.

About the logo we oppened a contest at the same time so at the moment there is no logo but the logo color will be simple.

The phone number will change so you can poste a random one for the design that i can change by myself.

i recieved many creation in both side BUT i want something in 1 side :)

Target Market(s)

Yoga student. all age

Industry/Entity Type

It Professional

Logo Text

Yoga fern

Font styles to use
Sans Serif

Requirements
Must have
• The text present on the docx
Nice to have
• Some symbols about yoga ( Namasté signs, mandala, ... )
Should not have
• Not too much details it has to be clear.

```html
<!DOCTYPE html>
<html lang="fr">
<head>
<meta charset="utf-8">
<title>Yoga fern – Stages d'été</title>
<link href="https://fonts.googleapis.com/css2?family=Bebas+Neue&family=Roboto:wght@400;700&display=swap" rel="stylesheet">
<style>
  :root{
    --backdrop:#4f4f4f;
    --sun-yellow:#e1c52e;
    --olive:#7e923c;
    --olive-deep:#5d6d2e;
    --lake:#325f6d;
    --lagoon:#00a799;
    --accent-yellow:#e9c62b;
    --paper-white:#ffffff;
    --logo-tint:#efdc86;
  }
  *{margin:0;padding:0;box-sizing:border-box}
  html,body{width:1200px;height:1200px;overflow:hidden}
  body{background:var(--backdrop);position:relative}
  .flyer{position:absolute;left:186px;top:14px;width:828px;height:1172px;overflow:hidden;background:var(--sun-yellow);color:var(--paper-white)}
  .flyer__bands{position:absolute;inset:0}
  .flyer__photo{position:absolute;left:240px;top:14px;width:380px;height:216px;border-radius:50% 50% 8px 8px / 70% 70% 8px 8px;background:radial-gradient(ellipse at 60% 55%,rgba(70,60,30,.55),rgba(120,100,40,.15) 70%,rgba(0,0,0,0) 100%)}
  .flyer__frame{position:absolute;inset:0}
  .logo-slot{position:absolute;left:22px;top:2px;width:105px;height:112px;background:var(--logo-tint);display:flex;flex-direction:column;align-items:center;justify-content:center;gap:6px}
  .logo-slot__mark{width:14px;height:14px;background:var(--paper-white)}
  .logo-slot__name{font-family:"Bebas Neue",sans-serif;font-size:30px;line-height:.9;text-align:center;color:var(--paper-white)}
  .kicker{position:absolute;left:0;right:0;top:10px;text-align:center;font-family:"Bebas Neue",sans-serif;font-size:60px;line-height:1}
  .title{position:absolute;left:0;right:0;top:60px;text-align:center;font-family:"Bebas Neue",sans-serif;font-size:172px;line-height:1;letter-spacing:1px}
  .intro{position:absolute;left:0;right:0;top:244px;text-align:center;font-family:"Bebas Neue",sans-serif;font-size:29px;line-height:33px}
  .schedule{position:absolute;left:0;right:0;top:450px;text-align:center;font-family:"Roboto",sans-serif;font-size:14.5px;line-height:19px}
  .schedule__month{color:var(--accent-yellow);font-weight:700;margin-top:6px}
  .schedule__month:first-child{margin-top:0}
  .schedule__title{font-weight:700}
  .schedule__group{margin-bottom:19px}
  .schedule__group--tight{margin-bottom:0}
  .closing{position:absolute;left:0;right:0;top:1056px;text-align:center;font-family:"Roboto",sans-serif;font-size:15.5px;line-height:20px}
  .sign-off{position:absolute;left:0;right:0;top:1124px;text-align:center;font-family:"Bebas Neue",sans-serif;font-size:38px;line-height:1}
</style>
</head>
<body>
<div class="flyer">
  <svg class="flyer__bands" viewBox="0 0 828 1172" width="828" height="1172" aria-hidden="true">
    <path d="M0 270 Q414 200 828 270 L828 1172 L0 1172 Z" fill="var(--olive)"/>
    <polygon points="300,240 260,480 0,760 0,640 180,380" fill="var(--olive-deep)" opacity=".55"/>
    <polygon points="560,240 600,480 828,700 828,560 680,380" fill="var(--olive-deep)" opacity=".55"/>
    <polygon points="340,240 480,240 560,480 300,480" fill="var(--olive-deep)" opacity=".6"/>
    <path d="M0 482 Q414 420 828 482 L828 1172 L0 1172 Z" fill="var(--lake)"/>
    <polygon points="250,470 300,470 170,1172 40,1172" fill="#fff" opacity=".07"/>
    <polygon points="360,470 420,470 420,1172 320,1172" fill="#fff" opacity=".05"/>
    <polygon points="560,470 620,470 820,1000 820,1120" fill="#fff" opacity=".07"/>
    <polygon points="0,540 120,470 0,700" fill="#fff" opacity=".06"/>
    <path d="M0 1078 Q414 1022 828 1078 L828 1172 L0 1172 Z" fill="var(--lagoon)"/>
  </svg>
  <div class="flyer__photo" role="img" aria-label="Photo d'une pratiquante de yoga en posture du cobra"></div>
  <svg class="flyer__frame" viewBox="0 0 828 1172" width="828" height="1172" aria-hidden="true">
    <g fill="none" stroke="var(--paper-white)" stroke-width="3">
      <polyline points="325,34 130,34"/>
      <polyline points="565,34 796,34 796,1141 520,1141"/>
      <polyline points="308,1141 30,1141 30,110"/>
    </g>
  </svg>
  <div class="logo-slot">
    <span class="logo-slot__mark"></span>
    <span class="logo-slot__name">Yoga<br>fern</span>
  </div>
  <div class="kicker">Nouvea</div>
  <div class="title">Yoga fern</div>
  <div class="intro">
    Nouveau !! Votre studio de yoga a Ixelles<br>
    Ouverture le 6 juin 2016 au<br>
    312 Rue des Tilleuls<br>
    1050 Ixelles<br>
    En attendant le planning des cours de la rentrée,<br>
    Yoga fern vous propose ses stages et ateliers d'été.
  </div>
  <div class="schedule">
    <p class="schedule__month">JUIN</p>
    <div class="schedule__group">
      <p class="schedule__title">Stage découverte du YOGA 10h00 85 € :</p>
      <p>Du lundi 6 au vendredi 10 juin : 10h00 à 12h00 ou 18h00 à 20h00</p>
      <p>Du lundi 13 au vendredi 17 juin : 10h00 à 12h00 ou 18h00 à 20h00</p>
      <p>Du lundi 20 au vendredi 24 juin : 10h00 à 12h00 ou 18h00 à 20h00</p>
      <p>Du lundi 27 au vendredi 1er juillet : 10h00 à 12h00 ou 18h00 à 20h00</p>
    </div>
    <div class="schedule__group schedule__group--tight">
      <p class="schedule__title">Atelier gestion du stress yoga/sophrologie 2h00 28 €</p>
      <p>Samedi 11 juin 10h30 à 12h30</p>
      <p>Samedi 11 juin 15h à 17h00</p>
      <p>Dimanche 12 juin 10h30 à 12h30</p>
      <p>Dimanche 12 juin 14h à 16h00</p>
    </div>
    <p class="schedule__month">JUILLET</p>
    <div class="schedule__group">
      <p class="schedule__title">Stage initiation à l'ASHTANGA 10h00 85 €</p>
      <p>Du lundi 4 au vendredi 8 juillet : 10h00 à 12h00 ou 18h00 à 20h00</p>
      <p>Du lundi 11 au vendredi 15 juillet : 10h00 à 12h00 ou 18h00 à 20h00</p>
      <p>Du lundi 18 au vendredi 22 juillet : 10h00 à 12h00 ou 18h00 à 20h00</p>
      <p>Du lundi 25 au vendredi 29 juillet : 10h00 à 12h00 ou 18h00 à 20h00</p>
    </div>
    <div class="schedule__group schedule__group--tight">
      <p class="schedule__title">Atelier gestion du stress yoga/sophrologie 2h00 28 €</p>
      <p>Samedi 9 juillet 10h30 à 12h30</p>
      <p>Samedi 9 juillet 15h00 à 17h00</p>
      <p>Dimanche 10 juillet 10h30 à 12h30</p>
      <p>Dimanche 10 juillet 14h00 à 16h00</p>
    </div>
    <p class="schedule__month">AOUT</p>
    <div class="schedule__group schedule__group--tight">
      <p class="schedule__title">Stage découverte du YOGA 10h00 85 €</p>
      <p>Du lundi 1er au vendredi 5 août : 10h00 à 12h00 ou 18h00 à 20h00</p>
      <p>Du lundi 8 au vendredi 12 août : 10h00 à 12h00 ou 18h00 à 20h00</p>
      <p>Du lundi 15 au vendredi 19 août : 10h00 à 12h00 ou 18h00 à 20h00</p>
      <p>Du lundi 22 au vendredi 26 août : 10h00 à 12h00 ou 18h00 à 20h00</p>
    </div>
  </div>
  <div class="closing">
    <p>Démarrage du planning annuel le 5 septembre 2016</p>
    <p>Plus d'info et inscription :</p>
    <p>Ou via notre page facebook : yoga fern</p>
  </div>
  <div class="sign-off">Un bel ete a tous</div>
</div>
</body>
</html>
```